Business Card Design - Crisp & Clean

Looking for a new clean and crisp business card design. Design must incorporate our corporate colors (see attached style sheet). We're a pretty fun loving group who likes to keep it light while still portraying a professional image. Card should incorporate both our logo and our mascot (see attachment). Card should be double sided and should have room for our social media - Facebook, Linked In and Twitter on the back. Font selections do not have to match the style guide.

```html
<!DOCTYPE html>
<html lang="en">
<head>
<meta charset="utf-8">
<title>BrightPeople Business Card</title>
<link rel="stylesheet" href="https://fonts.googleapis.com/css2?family=Roboto+Condensed:wght@300;400;700&display=swap">
<style>
  :root {
    --bg: #e9e7e3;
    --card: #ffffff;
    --ink: #1f1f1f;
    --ink-soft: #3a3a3a;
    --accent: #f5b400;
    --mascot-a: #f3e07a;
    --mascot-b: #d9d4c9;
    --shadow: rgba(0, 0, 0, 0.18);
  }
  * { box-sizing: border-box; margin: 0; padding: 0; }
  html, body {
    width: 1200px; height: 644px; overflow: hidden;
    background: var(--bg);
    font-family: "Roboto Condensed", Arial, sans-serif;
    color: var(--ink);
  }
  .canvas {
    width: 1200px; height: 644px;
    display: flex; align-items: center; justify-content: center; gap: 70px;
  }
  .card {
    background: var(--card);
    box-shadow: 0 10px 28px var(--shadow);
    position: relative;
    overflow: hidden;
  }
  /* Front (landscape) */
  .card-front {
    width: 520px; height: 297px;
    display: flex; align-items: center; justify-content: center;
  }
  .mascot {
    width: 260px; height: 210px; border-radius: 14px;
    background: radial-gradient(circle at 62% 62%, var(--mascot-a) 0 34%, var(--mascot-b) 70%, var(--card) 100%);
  }
  /* Back (portrait) */
  .card-back {
    width: 297px; height: 520px;
    padding: 56px 28px 26px;
    display: flex; flex-direction: column;
  }
  .brand { display: flex; flex-direction: column; gap: 5px; }
  .brand-row { display: flex; align-items: center; gap: 8px; }
  .brand-dot { width: 18px; height: 18px; border-radius: 50%; background: var(--accent); flex: none; }
  .brand-name { font-weight: 700; font-size: 24px; color: var(--ink); letter-spacing: 0.2px; }
  .brand-tagline { font-size: 6.5px; font-weight: 700; letter-spacing: 0.6px; color: var(--ink-soft); text-transform: uppercase; padding-left: 26px; }
  .details { margin-top: 64px; }
  .person-name { font-size: 27px; font-weight: 400; line-height: 1.05; }
  .person-title { font-size: 15px; font-weight: 300; margin-top: 3px; margin-bottom: 26px; }
  .contact-list { list-style: none; display: flex; flex-direction: column; gap: 8px; }
  .contact-item { display: flex; justify-content: space-between; align-items: center; font-size: 12.5px; color: var(--ink-soft); }
  .contact-icon { width: 12px; height: 12px; fill: var(--accent); flex: none; }
  .social-row {
    margin-top: auto;
    display: flex; justify-content: space-between;
    font-size: 11.5px; color: var(--ink-soft);
  }
  .social-item { display: flex; align-items: center; gap: 5px; white-space: nowrap; }
  .social-mark { width: 11px; height: 11px; border-radius: 50%; background: var(--accent); flex: none; }
</style>
</head>
<body>
<main class="canvas">
  <section class="card card-front" aria-label="Card front">
    <div class="mascot" role="img" aria-label="Company mascot illustration: cartoon inventor carrying a large yellow light bulb"></div>
  </section>

  <section class="card card-back" aria-label="Card back">
    <div class="brand">
      <div class="brand-row">
        <span class="brand-dot"></span>
        <span class="brand-name">BrightPeople</span>
      </div>
      <span class="brand-tagline">People process management solutions</span>
    </div>

    <div class="details">
      <h1 class="person-name">Dana Whitfield</h1>
      <p class="person-title">Marketing Wizard</p>
      <ul class="contact-list">
        <li class="contact-item"><span>4810 Maple Grove Lane</span>
          <svg class="contact-icon" viewBox="0 0 12 12"><path d="M6 0.5a4 4 0 0 0-4 4c0 3 4 7 4 7s4-4 4-7a4 4 0 0 0-4-4zm0 5.6a1.6 1.6 0 1 1 0-3.2 1.6 1.6 0 0 1 0 3.2z"/></svg></li>
        <li class="contact-item"><span>dana@brightpeople.com</span>
          <svg class="contact-icon" viewBox="0 0 12 12"><path d="M1 2.5h10v7H1z"/><path d="M1 2.5l5 4 5-4" fill="none" stroke="#fff" stroke-width="1"/></svg></li>
        <li class="contact-item"><span>555 - 010 - 2468</span>
          <svg class="contact-icon" viewBox="0 0 12 12"><path d="M3 1l2 2.4-1.2 1.4a7 7 0 0 0 3.4 3.4L8.6 7 11 9l-1.4 1.8C5.2 10.6 1.4 6.8 1.2 2.4z"/></svg></li>
        <li class="contact-item"><span>www.brightpeople.com</span>
          <svg class="contact-icon" viewBox="0 0 12 12"><circle cx="6" cy="6" r="5.2"/><path d="M1 6h10M6 0.8c-2.4 2.8-2.4 7.6 0 10.4M6 0.8c2.4 2.8 2.4 7.6 0 10.4" fill="none" stroke="#fff" stroke-width="0.8"/></svg></li>
      </ul>
    </div>

    <div class="social-row">
      <span class="social-item"><span class="social-mark"></span>dana.chirps</span>
      <span class="social-item"><span class="social-mark"></span>dana.works</span>
      <span class="social-item"><span class="social-mark"></span>dana.friends</span>
    </div>
  </section>
</main>
</body>
</html>
```